Business card for auto dealership

Looking for a clean modern design.
Would like attached logo incorporated

Industry/Entity Type

Car dealership

Contact Information for Business Card

Name, website, phone, cell, fax, email

```html
<!DOCTYPE html>
<html lang="en">
<head>
<meta charset="utf-8">
<title>Hollis Truck &amp; Auto Sales – Business Card</title>
<link rel="stylesheet" href="https://fonts.googleapis.com/css2?family=Roboto:wght@400;500;700&display=swap">
<style>
  :root {
    --backdrop: #9a9a9a;
    --card-white: #ffffff;
    --slate: #44566a;
    --slate-dark: #3a4a5c;
    --brand-red: #a8191e;
    --ink: #4a4f57;
    --ice: #b9d4ee;
  }
  * { box-sizing: border-box; margin: 0; padding: 0; }
  html, body {
    width: 1200px;
    height: 801px;
    overflow: hidden;
    background: var(--backdrop);
    font-family: "Roboto", Arial, sans-serif;
  }
  .stage {
    width: 1200px;
    height: 801px;
    display: flex;
    align-items: center;
    justify-content: center;
    gap: 48px;
  }
  .card {
    width: 525px;
    height: 300px;
    border-radius: 14px;
    box-shadow: 0 10px 24px rgba(0, 0, 0, 0.25);
    position: relative;
    overflow: hidden;
  }

  /* Front */
  .card--front {
    background: var(--card-white);
    display: flex;
    align-items: center;
  }
  .front__brand {
    width: 262px;
    padding-left: 40px;
    display: flex;
    align-items: center;
    gap: 10px;
  }
  .brand-dot {
    width: 14px;
    height: 14px;
    border-radius: 50%;
    background: var(--slate);
    flex: none;
  }
  .brand-name {
    color: var(--slate);
    font-weight: 700;
    line-height: 1.05;
  }
  .front__brand .brand-name { font-size: 30px; }
  .brand-name small {
    display: block;
    font-size: 0.42em;
    letter-spacing: 0.06em;
    text-transform: uppercase;
    margin-top: 4px;
  }
  .front__divider {
    width: 1.5px;
    height: 118px;
    background: var(--brand-red);
    flex: none;
  }
  .front__contact {
    padding-left: 26px;
  }
  .person-name {
    color: var(--brand-red);
    font-weight: 500;
    font-size: 22px;
    letter-spacing: 0.03em;
    text-transform: uppercase;
  }
  .person-role {
    color: var(--ink);
    font-size: 12px;
    letter-spacing: 0.04em;
    text-transform: uppercase;
    margin: 2px 0 10px;
  }
  .contact-list { list-style: none; }
  .contact-list li {
    display: flex;
    align-items: center;
    gap: 8px;
    color: var(--ink);
    font-size: 13px;
    line-height: 19px;
  }
  .contact-list svg {
    width: 10px;
    height: 10px;
    flex: none;
    fill: none;
    stroke: var(--brand-red);
    stroke-width: 1.6;
  }

  /* Back */
  .card--back {
    background: linear-gradient(160deg, var(--slate) 0%, var(--slate-dark) 100%);
    display: flex;
    align-items: center;
    justify-content: center;
  }
  .back__brand {
    display: flex;
    align-items: center;
    gap: 14px;
  }
  .back__brand .brand-dot {
    width: 20px;
    height: 20px;
    background: var(--ice);
  }
  .back__brand .brand-name {
    color: var(--ice);
    font-size: 52px;
  }
</style>
</head>
<body>
<main class="stage">

  <section class="card card--front" aria-label="Business card front">
    <div class="front__brand">
      <span class="brand-dot"></span>
      <p class="brand-name">Hollis<small>Truck &amp; Auto Sales</small></p>
    </div>
    <div class="front__divider"></div>
    <div class="front__contact">
      <h1 class="person-name">Daniel Reeve</h1>
      <p class="person-role">Director</p>
      <ul class="contact-list">
        <li>
          <svg viewBox="0 0 10 10"><path d="M2 1l2 2-1 1.2c.6 1.2 1.5 2.1 2.8 2.8L7 6l2 2-1.2 1.2C4.5 9 1 5.5.8 2.2z"/></svg>
          +330 555-0142
        </li>
        <li>
          <svg viewBox="0 0 10 10"><rect x="2.5" y="0.8" width="5" height="8.4" rx="1"/><path d="M4.3 7.6h1.4"/></svg>
          +330 555-0187
        </li>
        <li>
          <svg viewBox="0 0 10 10"><rect x="0.8" y="2" width="8.4" height="6" rx="0.6"/><path d="M1 2.4l4 3 4-3"/></svg>
          info@hollisauto.com
        </li>
        <li>
          <svg viewBox="0 0 10 10"><circle cx="5" cy="5" r="4.2"/><path d="M0.8 5h8.4M5 0.8c-2.2 2.4-2.2 6 0 8.4M5 0.8c2.2 2.4 2.2 6 0 8.4"/></svg>
          www.hollisauto.com
        </li>
      </ul>
    </div>
  </section>

  <section class="card card--back" aria-label="Business card back">
    <div class="back__brand">
      <span class="brand-dot"></span>
      <p class="brand-name">Hollis<small>Truck &amp; Auto Sales</small></p>
    </div>
  </section>

</main>
</body>
</html>
```